Professional services business card

This is for a new business in New Zealand, providing professional advice to boards of directors of companies
The point of difference is a strong blend of Financial and IT knowledge

Target audience are senior business executives, CEO/CFO/President, etc.
So, simple but appealing
Business colours are orange and blue

Sample logo attached
proposed Content also attached - feedback on wording is welcome
Updates

Please provide for a logo to be added - about 30 mm wide and 10 mm high

the company name is "Corvel Waypoint Ltd" - logo now uploaded to the project brief

Information to include are now in the second file that was uploaded

Industry/Entity Type

Business

```html
<!DOCTYPE html>
<html lang="en">
<head>
<meta charset="utf-8">
<title>Corvel Waypoint Ltd — Business Card</title>
<link rel="stylesheet" href="https://fonts.googleapis.com/css2?family=Questrial&display=swap">
<style>
  :root {
    --orange: #e08a2c;
    --orange-deep: #d27b1f;
    --blue: #1f8bc4;
    --paper: #ffffff;
    --backdrop: #ececec;
    --ink-soft: #5a5a5a;
  }
  * { box-sizing: border-box; margin: 0; padding: 0; }
  html, body { width: 1200px; height: 900px; overflow: hidden; }
  body {
    background: var(--backdrop);
    font-family: "Questrial", "Century Gothic", sans-serif;
    position: relative;
  }
  .card {
    position: absolute;
    top: 300px;
    width: 540px;
    height: 300px;
    overflow: hidden;
    box-shadow: 0 2px 6px rgba(0,0,0,0.12);
  }
  .card--front { left: 40px; background: var(--paper); }
  .card--back { left: 620px; background: var(--orange); }

  /* Front */
  .wordmark {
    position: absolute;
    display: flex;
    align-items: center;
    gap: 8px;
    color: var(--blue);
    font-size: 26px;
    letter-spacing: 0.5px;
  }
  .wordmark__dot {
    width: 14px; height: 14px;
    border-radius: 50%;
    background: var(--orange);
  }
  .card--front .wordmark { left: 34px; top: 40px; }
  .front__rule {
    position: absolute;
    left: 0; right: 0; top: 112px;
    height: 2px;
    background: var(--orange);
  }
  .contact {
    position: absolute;
    left: 34px; top: 128px;
    color: var(--blue);
  }
  .contact__name { font-size: 17px; font-weight: 700; }
  .contact__creds { font-weight: 400; }
  .contact__company { font-size: 11px; font-weight: 700; margin-top: 6px; }
  .contact__line {
    display: flex; align-items: center; gap: 6px;
    font-size: 11px; margin-top: 3px;
  }
  .contact__line svg { width: 10px; height: 10px; flex: none; }
  .front__band {
    position: absolute;
    left: 0; right: 0; bottom: 0;
    height: 44px;
    background: var(--orange);
    display: flex; align-items: center;
    padding-left: 34px;
    color: var(--paper);
    font-size: 12px;
  }

  /* Back */
  .card--back .wordmark { left: 34px; top: 40px; }
  .topics {
    position: absolute;
    left: 300px; top: 128px;
    padding-left: 12px;
    border-left: 1px solid rgba(255,255,255,0.8);
    color: var(--paper);
    list-style: none;
  }
  .topics__title { font-size: 11px; font-weight: 700; letter-spacing: 0.5px; margin-bottom: 3px; }
  .topics__item {
    display: flex; align-items: center; gap: 6px;
    font-size: 12px; line-height: 1.5;
  }
  .topics__item svg { width: 9px; height: 9px; flex: none; }
</style>
</head>
<body>

<section class="card card--front" aria-label="Business card front">
  <div class="wordmark"><span class="wordmark__dot"></span><span>Corvel Waypoint</span></div>
  <div class="front__rule"></div>
  <div class="contact">
    <p class="contact__name">Ana Reiter<span class="contact__creds">, M.Com, ACA(NZ), ACMA</span></p>
    <p class="contact__company">Corvel Waypoint Ltd</p>
    <p class="contact__line">
      <svg viewBox="0 0 10 10"><circle cx="5" cy="5" r="4.4" fill="none" stroke="currentColor" stroke-width="1"/><path d="M3.4 2.8l1 1-0.6 0.7c0.4 0.8 1 1.4 1.8 1.8l0.7-0.6 1 1-0.8 0.8C4.9 7.2 2.8 5.1 2.6 3.6z" fill="currentColor"/></svg>
      021 555 0174
    </p>
    <p class="contact__line">
      <svg viewBox="0 0 10 10"><rect x="0.5" y="2" width="9" height="6" fill="currentColor"/><path d="M0.8 2.3L5 5.5l4.2-3.2" fill="none" stroke="#fff" stroke-width="0.8"/></svg>
      Ana.Reiter@corvelwaypoint.com
    </p>
    <p class="contact__line">
      <svg viewBox="0 0 10 10"><rect x="0.5" y="0.5" width="9" height="9" fill="currentColor"/></svg>
      /in/anareiter
    </p>
  </div>
  <div class="front__band">PO Box 40217, Harbour Lane, Wellington, 6011</div>
</section>

<section class="card card--back" aria-label="Business card back">
  <div class="wordmark"><span class="wordmark__dot" style="background:#fff"></span><span>Corvel Waypoint</span></div>
  <ul class="topics">
    <li class="topics__title">TALK TO US ABOUT</li>
    <li class="topics__item"><svg viewBox="0 0 10 10"><path d="M1 9L8 2M4 2h4v4" fill="none" stroke="#fff" stroke-width="1.2"/></svg>Governance</li>
    <li class="topics__item"><svg viewBox="0 0 10 10"><path d="M1 9L8 2M4 2h4v4" fill="none" stroke="#fff" stroke-width="1.2"/></svg>Good Stewardship</li>
    <li class="topics__item"><svg viewBox="0 0 10 10"><path d="M1 9L8 2M4 2h4v4" fill="none" stroke="#fff" stroke-width="1.2"/></svg>Financial Insight</li>
    <li class="topics__item"><svg viewBox="0 0 10 10"><path d="M1 9L8 2M4 2h4v4" fill="none" stroke="#fff" stroke-width="1.2"/></svg>Information Technology Insight</li>
    <li class="topics__item"><svg viewBox="0 0 10 10"><path d="M1 9L8 2M4 2h4v4" fill="none" stroke="#fff" stroke-width="1.2"/></svg>Mentoring and Business Advice</li>
  </ul>
</section>

</body>
</html>
```